Vegan Jerky company needs a label for it's pouch, and a new logo

Dear Designers - this used to be a guaranteed project, however, due to the low quality of designs I have received, I have removed the guaranteed status. However, we need this product made and we will pay for a great, high quality design that meets the requirements of our brief.

We need sticker labels that will go onto the front and back of our vegan jerky package. Our package is a zip-sealable pouch, and we will either go with black, white or brown for the color of the pouch.

We need the concept, artwork, theme and logo designed. Pls choose the colors.

There will be four flavors. These can be finished as part of another project. The flavors are: Smoked Maple, Cracked Pepper, Teriyaki Sriracha, Original.

We are Lonny and Marva's Vegan Jerky.

Our food is vegan, non GMO, straight from the farm, organic, healthy, pure, clean, made in small batches and earth friendly. We use no chemicals or artificial flavors and our product is 100% natural.

Our kitchen is yours.
Updates

Low designer entries

Target Market(s)

Vegetarians, vegans, health conscious, ecological, intelligent, caring.

Industry/Entity Type

Food Production

Logo Text

"Lonny and Marva" and "Our Kitchen is Yours"

Colors

Designer to choose colors to be used in the design.

Requirements
Must have
• earth friendly design, classy, hipster, vegan design, shabby chic,
Nice to have
• i have no ideas really...
• We prefer black and while, with a little splash of color. The last file is an idea I had but please use your own vision.

```html
<!DOCTYPE html>
<html lang="en">
<head>
<meta charset="utf-8">
<title>Lonny &amp; Marva's Vegan Jerky – Label</title>
<link rel="stylesheet" href="https://fonts.googleapis.com/css2?family=Kaushan+Script&display=swap">
<style>
  :root {
    --paper: #ffffff;
    --label-cream: #fdfbca;
    --label-edge: #ece9b4;
    --ink: #1b1613;
    --taupe: #948372;
    --mark-grey: #8a8a8a;
  }
  html, body {
    margin: 0;
    padding: 0;
    width: 1200px;
    height: 971px;
    overflow: hidden;
    background: var(--paper);
  }
  .label {
    display: block;
    width: 1200px;
    height: 971px;
    font-family: "Kaushan Script", cursive;
  }
  .label__oval { fill: var(--label-cream); stroke: var(--label-edge); stroke-width: 2; }
  .label__brand { fill: var(--ink); font-size: 128px; }
  .label__star { fill: var(--ink); }
  .label__product { fill: var(--taupe); font-size: 96px; }
  .label__claim { fill: var(--ink); font-size: 26px; }
  .label__mark-square { fill: var(--mark-grey); }
  .label__mark-name { fill: var(--ink); font-size: 38px; }
</style>
</head>
<body>
<svg class="label" viewBox="0 0 1200 971" xmlns="http://www.w3.org/2000/svg" role="img" aria-label="Lonny and Marva's Vegan Jerky label">
  <defs>
    <path id="brand-arc" d="M 95 560 A 505 355 0 0 1 1105 560"/>
    <path id="claim-arc" d="M 232 777 Q 598 989 966 777"/>
  </defs>

  <ellipse class="label__oval" cx="600" cy="486" rx="596" ry="478"/>

  <text class="label__brand">
    <textPath href="#brand-arc" startOffset="50%" text-anchor="middle" textLength="1230" lengthAdjust="spacing">Lonny &amp; Marva's</textPath>
  </text>

  <g class="label__mark">
    <rect class="label__mark-square" x="468" y="428" width="34" height="34"/>
    <text class="label__mark-name" x="514" y="458">Lonny &amp; Marva</text>
  </g>

  <polygon class="label__star" points="160,614 166,631 184,631 170,642 175,659 160,649 145,659 150,642 136,631 154,631"/>
  <polygon class="label__star" points="1052,614 1058,631 1076,631 1062,642 1067,659 1052,649 1037,659 1042,642 1028,631 1046,631"/>

  <text class="label__product" x="604" y="728" text-anchor="middle">Vegan Jerky</text>

  <text class="label__claim">
    <textPath href="#claim-arc" startOffset="50%" text-anchor="middle">No Chemicals or Artificial Flavors - 100% Natural.</textPath>
  </text>
</svg>
</body>
</html>
```